Wendlow Cellars -responsive, bootstrap website design

Looking to build a responsive service website.

Logo and pictures have been provided.

PLEASE REVIEW ATTACHED DESIGN STYLE GUIDES & CLIENT CREATIVE BRIEF FOR OUR REQUIREMENT. THANK YOU AND GOOD LUCK!

```html
<!DOCTYPE html>
<html lang="en">
<head>
<meta charset="utf-8">
<title>Wendlow Cellars</title>
<link rel="stylesheet" href="https://fonts.googleapis.com/css2?family=Noto+Serif&family=Roboto:wght@300;400&display=swap">
<style>
  :root {
    --gold: #b8954a;
    --white: #ffffff;
    --rule: #e4e4e4;
    --panel: rgba(118, 96, 8, 0.78);
    --panel-line: rgba(255, 240, 190, 0.55);
    --footer-bg: rgba(20, 24, 10, 0.82);
    --footer-text: #f2f2f2;
    --ink: #1e1e1e;
  }
  * { box-sizing: border-box; margin: 0; padding: 0; }
  html, body { width: 1200px; height: 994px; overflow: hidden; }
  body { position: relative; font-family: "Roboto", Arial, sans-serif; font-weight: 300; }

  .hero-scene {
    position: absolute; inset: 0;
    background: linear-gradient(180deg,
      #8fb8d6 0%, #b9d2dd 18%, #c8d7cf 24%, #6f8f7a 27%,
      #5f9a3e 33%, #7fb33a 42%, #8bbf35 52%, #7cad2c 64%,
      #4f8a22 78%, #3a6a1c 88%, #4a4a1c 100%);
  }

  .site-header {
    position: absolute; top: 0; left: 0; width: 1200px; height: 75px;
    background: var(--white);
    box-shadow: 0 2px 6px rgba(0,0,0,0.18);
  }
  .site-header::before, .site-header::after {
    content: ""; position: absolute; left: 72px; right: 68px; height: 1px; background: var(--rule);
  }
  .site-header::before { top: 11px; }
  .site-header::after { top: 64px; }
  .main-nav a {
    position: absolute; top: 28px; font-size: 16px; color: var(--gold); text-decoration: none;
    transform: translateX(-50%); white-space: nowrap;
  }

  .brand-tab {
    position: absolute; top: 0; left: 505px; width: 193px; height: 148px;
    background: var(--white);
    clip-path: polygon(0 0, 100% 0, 100% 88%, 92% 100%, 8% 100%, 0 88%);
    display: flex; align-items: center; justify-content: center;
    filter: drop-shadow(0 2px 3px rgba(0,0,0,0.2));
  }
  .brand-name {
    font-family: "Noto Serif", Georgia, serif; font-size: 24px; color: var(--ink);
    text-align: center; line-height: 1.15;
  }

  .tagline {
    position: absolute; top: 364px; left: 0; width: 1200px; text-align: center;
    font-family: "Noto Serif", Georgia, serif; font-size: 40px; color: var(--white);
    text-shadow: 1px 2px 4px rgba(0,0,0,0.55);
  }

  .intro-panel {
    position: absolute; top: 449px; left: 208px; width: 786px; height: 204px;
  }
  .intro-panel svg.panel-frame { position: absolute; inset: 0; }
  .intro-icon { position: absolute; top: 24px; left: 385px; }
  .intro-text {
    position: absolute; top: 72px; left: 68px; width: 650px; text-align: center;
    font-size: 16px; line-height: 24.5px; color: var(--white);
  }

  .site-footer {
    position: absolute; left: 0; top: 935px; width: 1200px; height: 59px;
    background: var(--footer-bg); font-size: 13px; font-weight: 400;
  }
  .footer-meta { position: absolute; left: 71px; top: 22px; color: var(--footer-text); white-space: pre; }
  .footer-links { position: absolute; right: 69px; top: 22px; color: var(--gold); white-space: pre; }
  .footer-links a { color: var(--gold); text-decoration: none; }
</style>
</head>
<body>
  <div class="hero-scene" role="img" aria-label="Sunlit vineyard rows in a green valley with rolling fields and a barn under a blue sky"></div>

  <header class="site-header">
    <nav class="main-nav">
      <a href="#" style="left:228px">Home</a>
      <a href="#" style="left:323px">About</a>
      <a href="#" style="left:420px">Wines</a>
      <a href="#" style="left:779px">Store</a>
      <a href="#" style="left:868px">News</a>
      <a href="#" style="left:968px">Join Us</a>
    </nav>
  </header>
  <div class="brand-tab"><span class="brand-name">Wendlow<br>Cellars</span></div>

  <h1 class="tagline">We make wine that speaks to us through the soil.</h1>

  <section class="intro-panel">
    <svg class="panel-frame" width="786" height="204" viewBox="0 0 786 204">
      <polygon points="18,0 768,0 786,18 786,186 768,204 18,204 0,186 0,18" fill="var(--panel)"/>
      <polygon points="26,10 760,10 776,26 776,178 760,194 26,194 10,178 10,26" fill="none" stroke="var(--panel-line)" stroke-width="1"/>
      <line x1="72" y1="38" x2="714" y2="38" stroke="var(--panel-line)" stroke-width="1"/>
    </svg>
    <svg class="intro-icon" width="16" height="28" viewBox="0 0 16 28">
      <rect x="2" y="0" width="12" height="22" fill="var(--panel)"/>
      <path d="M3 1 H13 V7 C13 11 10 13 8 13 C6 13 3 11 3 7 Z" fill="#fff"/>
      <rect x="7.2" y="13" width="1.6" height="9" fill="#fff"/>
      <rect x="4" y="22" width="8" height="1.6" fill="#fff"/>
    </svg>
    <p class="intro-text">Our vineyards are all located in the heart of the Walla Walla Valley.&nbsp; Each vineyard is treated to ideal sun exposure and is made up of incredibly rich soil.&nbsp; State-of-the-art trellis systems provide the vines optimal room to grow grapes of the highest quality and complexity.</p>
  </section>

  <footer class="site-footer">
    <div class="footer-meta">wendlow cellars  |   walla walla, washington   |   ©2014. all rights reserved</div>
    <div class="footer-links"><a href="#">Contact Us</a>   |   <a href="#">Facenote</a>   |   <a href="#">Chirpline</a></div>
  </footer>
</body>
</html>
```